Gilded Realty website

full website from start to finish. I would like something like this -
https://www.brindlecovemanors.com/
http://plumhavenlots.com/

Target Market(s)

real estate investors

Industry/Entity Type

Real Estate

Number of Pages Required

5+ page

Font styles to use
Sans Serif

Colors

Designer to choose colors to be used in the design.

Requirements
Must have
• translated in English, Spanish and japanese

```html
<!DOCTYPE html>
<html lang="en">
<head>
<meta charset="utf-8">
<title>Gilded Realty</title>
<link rel="stylesheet" href="https://fonts.googleapis.com/css2?family=Montserrat:wght@300;400;500;600;700;800&family=Playfair+Display:wght@900&display=swap">
<style>
:root{
  --red:#d0282e;
  --ink:#222;
  --muted:#666;
  --ghost:#f3f3f3;
  --white:#fff;
}
*{margin:0;padding:0;box-sizing:border-box}
html,body{width:1200px;height:1200px;overflow:hidden;background:var(--white);font-family:'Montserrat',sans-serif;color:var(--ink)}
.page{position:relative;width:1200px;height:1200px;overflow:hidden}
.hero{position:absolute;left:0;top:0;width:1200px;height:576px;
  background:linear-gradient(180deg,#5b4a6a 0%,#b8788a 14%,#8e8590 26%,#5e5a5c 42%,#6d5a47 60%,#4e4a46 78%,#5a5755 100%)}
.hero-glow{position:absolute;left:0;top:250px;width:1200px;height:200px;
  background:radial-gradient(ellipse at 40% 50%,rgba(230,170,80,.35),rgba(0,0,0,0) 60%)}
.header{position:absolute;left:0;top:0;width:1200px;height:80px;color:var(--white)}
.brand{position:absolute;left:144px;top:27px;font-size:19px;font-weight:700;letter-spacing:.3px}
.divider{position:absolute;left:298px;top:22px;width:1px;height:30px;background:rgba(255,255,255,.3)}
.phone{position:absolute;left:307px;top:31px;font-size:10px;display:flex;align-items:center;gap:7px}
.social{position:absolute;left:556px;top:35px;display:flex;gap:15px}
.social span{width:12px;height:12px;border-radius:50%;background:var(--white)}
.nav{position:absolute;left:785px;top:32px;display:flex;gap:28px;font-size:11.5px;font-weight:600}
.menu{position:absolute;left:1039px;top:32px;width:17px}
.menu i{display:block;height:2px;background:var(--white);margin-bottom:5px}
.slide-no{position:absolute;left:140px;top:352px;font-size:78px;font-weight:800;color:var(--white);letter-spacing:-2px;line-height:1}
.dots{position:absolute;left:144px;top:452px;display:flex;gap:12px}
.dots i{width:24px;height:2px;background:rgba(255,255,255,.4)}
.dots i.on{height:3px;background:var(--white)}
.hero-title{position:absolute;left:141px;top:462px;font-size:42px;font-weight:700;color:var(--white)}
.cta{position:absolute;left:144px;top:545px;width:176px;height:48px;background:var(--red);color:var(--white);
  font-size:11.5px;font-weight:700;letter-spacing:1px;display:flex;align-items:center;justify-content:center;box-shadow:0 8px 18px rgba(0,0,0,.12)}
.ghost-word{position:absolute;left:10px;top:580px;font-family:'Playfair Display',serif;font-weight:900;font-size:196px;color:var(--ghost);letter-spacing:-4px;line-height:1}
.intro{position:absolute;left:142px;top:708px;width:270px}
.intro h2{font-size:41px;font-weight:300;line-height:42px;color:#1a1a1a}
.intro h3{margin-top:20px;font-size:13.5px;font-weight:600;color:var(--red)}
.intro p{margin-top:18px;margin-left:3px;font-size:12.5px;line-height:19.2px;color:var(--muted)}
.arrows{position:absolute;left:229px;top:997px}
.card{position:absolute;top:679px;width:280px}
.card .photo{height:340px}
.card .buy{position:absolute;left:185px;top:316px;width:81px;height:40px;background:var(--red);color:var(--white);
  font-size:11.5px;font-weight:700;display:flex;align-items:center;justify-content:center}
.card h4{margin-top:30px;font-size:15px;font-weight:600;letter-spacing:1px}
.card small{display:block;margin-top:9px;font-size:9.5px;font-weight:500;color:var(--muted)}
.band-left{position:absolute;left:0;top:1170px;width:600px;height:30px;background:linear-gradient(90deg,#3b2a22,#6d4a35,#3a2a22)}
.band-right{position:absolute;left:600px;top:1170px;width:600px;height:30px;background:linear-gradient(90deg,#8c9297,#b5aea5,#7d5a40)}
</style>
</head>
<body>
<div class="page">
  <section class="hero" role="img" aria-label="Stone luxury mansion at dusk with lit windows under a pink sky">
    <div class="hero-glow"></div>
  </section>

  <header class="header">
    <div class="brand">GILDED REALTY</div>
    <div class="divider"></div>
    <div class="phone">
      <svg width="10" height="10" viewBox="0 0 24 24" fill="#fff"><path d="M6.6 10.8a15 15 0 0 0 6.6 6.6l2.2-2.2c.3-.3.7-.4 1-.2 1.1.4 2.3.6 3.6.6.6 0 1 .4 1 1V20c0 .6-.4 1-1 1A17 17 0 0 1 3 4c0-.6.4-1 1-1h3.5c.6 0 1 .4 1 1 0 1.3.2 2.5.6 3.6.1.3 0 .7-.2 1z"/></svg>
      +1(02) 555 0148
    </div>
    <div class="social"><span></span><span></span><span></span><span></span></div>
    <nav class="nav"><span>OUR PROPERTIES</span><span>PLATINUM CLUB</span></nav>
    <div class="menu"><i></i><i></i><i></i></div>
  </header>

  <div class="slide-no">02</div>
  <div class="dots"><i></i><i class="on"></i><i></i><i></i></div>
  <h1 class="hero-title">Luxury Palace</h1>
  <div class="cta">SEARCH ALL HOMES</div>

  <div class="ghost-word">Featured</div>

  <div class="intro">
    <h2>Featured<br>Home</h2>
    <h3>Dummy text of the printing etting</h3>
    <p>Lorem ipsum dolor sit amet, consectetur adipisicing elit, sed do eiusmod tempor incididunt ut labore et dolore magna aliqua. Ut enim ad minim veniam, quis nostrud exercitation.</p>
  </div>

  <svg class="arrows" width="80" height="30" viewBox="0 0 80 30">
    <circle cx="13" cy="13" r="12.5" fill="none" stroke="#aaa" stroke-width="1"/>
    <path d="M15 8 l-5 5 5 5" fill="none" stroke="#888" stroke-width="1"/>
    <circle cx="64" cy="13" r="12.5" fill="none" stroke="#222" stroke-width="1.3"/>
    <path d="M35 13 H70 M64 7 l6 6 -6 6" fill="none" stroke="#222" stroke-width="1.3"/>
  </svg>

  <article class="card" style="left:449px">
    <div class="photo" role="img" aria-label="Wooden chalet among pine trees in deep snow" style="background:linear-gradient(180deg,#dfe3e6 0%,#8a6a48 45%,#e9edf0 70%,#f4f6f8 100%)"></div>
    <div class="buy">BUY</div>
    <h4>Location/Geneva</h4>
    <small>Deposit of32in basement</small>
  </article>

  <article class="card" style="left:753px">
    <div class="photo" role="img" aria-label="White grand hall interior with twin staircases and a decorated tree" style="background:linear-gradient(180deg,#eef0f1 0%,#e2dcd6 45%,#9c7a62 75%,#6b4e3d 100%)"></div>
    <div class="buy">BUY</div>
    <h4>Sale/Vucherens</h4>
    <small>On plans - Spacious contiguous villa of4.5</small>
  </article>

  <article class="card" style="left:1057px">
    <div class="photo" role="img" aria-label="Pastel Mediterranean villa facade with palm trees" style="background:linear-gradient(90deg,#7f9a86 0%,#cfd8d8 40%,#a9c0bc 100%)"></div>
    <h4>Location/Geneva</h4>
    <small>Deposit of32in basement</small>
  </article>

  <div class="band-left" role="img" aria-label="Warm wood interior ceiling"></div>
  <div class="band-right" role="img" aria-label="House exterior with timber pergola"></div>
</div>
</body>
</html>
```